Business Card Design for company

We want new business cards. We'd like something different-- yet still highly professional. Our tagline is Providing leadership, delivering success. Stock photos are ok, as long as they are relevant and look upscale.

Target Market(s)

Architecture/Business Management Consulting/Engineering Consulting

Contact Information for Business Card

dark gray background with pops of blue might be good, but you tell me. You're the designers. Rounded corners might be nice, but again, you tell me.

Font styles to use
Serif
Sans Serif

Colors
3276b5
5c5c5c
9d9d9d
fbfbfb

Requirements
Nice to have
• Something different, but still very professional.

```html
<!DOCTYPE html>
<html lang="en">
<head>
<meta charset="utf-8">
<title>Norvale Group – Business Cards</title>
<link href="https://fonts.googleapis.com/css2?family=Open+Sans:wght@400;600;700&display=swap" rel="stylesheet">
<style>
  :root {
    --blue: #3276b5;
    --charcoal: #5c5c5c;
    --grey: #9d9d9d;
    --card: #fbfbfb;
    --backdrop: #e4e4e4;
    --ink: #3a3a3a;
  }
  * { margin: 0; padding: 0; box-sizing: border-box; }
  html, body { width: 1200px; height: 1200px; overflow: hidden; }
  body {
    background: var(--backdrop);
    font-family: "Open Sans", Arial, sans-serif;
    position: relative;
  }
  .card {
    position: absolute;
    left: 300px;
    width: 600px;
    height: 340px;
    background: var(--card);
    overflow: hidden;
  }
  .card--front { top: 188px; }
  .card--back { top: 675px; }

  /* front */
  .accent-bar {
    position: absolute;
    height: 10px;
    background: var(--grey);
  }
  .accent-bar--top { left: 0; top: 62px; width: 290px; }
  .accent-bar--bottom { right: 0; top: 284px; width: 242px; }
  .front-brand {
    position: absolute;
    left: 0; right: 0; top: 108px;
    text-align: center;
    color: var(--blue);
    font-weight: 600;
    line-height: 1;
  }
  .front-brand__main { display: block; font-size: 60px; letter-spacing: 1px; }
  .front-brand__sub { display: block; font-size: 20px; letter-spacing: 4px; margin-top: 6px; color: var(--charcoal); }
  .front-tagline {
    position: absolute;
    left: 0; right: 0; top: 222px;
    text-align: center;
    font-size: 11px;
    font-weight: 400;
    letter-spacing: 1px;
    color: var(--charcoal);
  }
  .front-web {
    position: absolute;
    left: 0; right: 0; top: 248px;
    text-align: center;
    font-size: 12px;
    font-weight: 700;
    color: var(--ink);
  }

  /* back */
  .side-accent {
    position: absolute;
    top: 95px;
    width: 70px;
    height: 160px;
  }
  .side-accent--left {
    left: 0;
    background: linear-gradient(90deg, #b4b4b4, rgba(251,251,251,0));
  }
  .side-accent--right {
    right: 0;
    background: linear-gradient(270deg, #b4b4b4, rgba(251,251,251,0));
  }
  .back-brand {
    position: absolute;
    left: 0; right: 0; top: 24px;
    text-align: center;
    color: var(--blue);
    font-weight: 600;
    line-height: 1;
  }
  .back-brand__main { display: block; font-size: 28px; letter-spacing: 1px; }
  .back-brand__sub { display: block; font-size: 9px; letter-spacing: 2px; margin-top: 3px; color: var(--charcoal); }
  .person-name {
    position: absolute;
    left: 0; right: 0; top: 88px;
    text-align: center;
    font-size: 32px;
    font-weight: 400;
    color: var(--charcoal);
  }
  .contact-map { position: absolute; left: 165px; top: 145px; width: 90px; height: 140px; }
  .contact-line {
    position: absolute;
    font-size: 11px;
    font-weight: 600;
    color: var(--ink);
    line-height: 1.35;
  }
  .contact-line--phone { left: 222px; top: 155px; }
  .contact-line--email { left: 250px; top: 205px; }
  .contact-line--address { left: 222px; top: 258px; }
</style>
</head>
<body>

<section class="card card--front">
  <div class="accent-bar accent-bar--top"></div>
  <div class="front-brand">
    <span class="front-brand__main">NORVALE</span>
    <span class="front-brand__sub">GROUP</span>
  </div>
  <p class="front-tagline">Providing leadership, delivering success</p>
  <p class="front-web">www.norvalegroup.com</p>
  <div class="accent-bar accent-bar--bottom"></div>
</section>

<section class="card card--back">
  <div class="side-accent side-accent--left" role="img" aria-label="Geometric side ornament in grey"></div>
  <div class="side-accent side-accent--right" role="img" aria-label="Geometric side ornament in grey"></div>

  <div class="back-brand">
    <span class="back-brand__main">NORVALE</span>
    <span class="back-brand__sub">GROUP</span>
  </div>
  <h1 class="person-name">Daniel Reyes</h1>

  <svg class="contact-map" viewBox="0 0 90 140" aria-hidden="true">
    <g stroke="#5c5c5c" stroke-width="1.5" fill="none">
      <line x1="16" y1="18" x2="60" y2="68"/>
      <line x1="60" y1="68" x2="16" y2="122"/>
    </g>
    <g fill="#fbfbfb" stroke="#5c5c5c" stroke-width="1.5">
      <circle cx="16" cy="18" r="8"/>
      <circle cx="60" cy="68" r="8"/>
      <circle cx="16" cy="122" r="8"/>
    </g>
    <path d="M12.5 14.5 q1-1 2 0 l1 1.5 q.5 1-.5 1.5 q1 2 2.5 3 q.5-1 1.5-.5 l1.5 1 q1 1 0 2 q-1.5 1.5-4-.5 q-3-2.5-4.5-5 q-1-2 .5-3z" fill="#5c5c5c"/>
    <rect x="55" y="64.5" width="10" height="7" fill="#5c5c5c"/>
    <polyline points="55,64.5 60,68.5 65,64.5" fill="none" stroke="#fbfbfb" stroke-width="1"/>
    <path d="M16 127 q-4-4.5-4-7 a4 4 0 0 1 8 0 q0 2.5-4 7z" fill="#5c5c5c"/>
    <circle cx="16" cy="120" r="1.4" fill="#fbfbfb"/>
  </svg>

  <p class="contact-line contact-line--phone">1 (555) 013-2747</p>
  <p class="contact-line contact-line--email">INFO@NORVALEGROUP.COM</p>
  <p class="contact-line contact-line--address">4180 Harbor View Lane<br>Tampa, FL 33602</p>
</section>

</body>
</html>
```